Modern Business Card

Modern professional business card with more than just logo and demographic info. Something memorable.

We are a trendy/modern chiropractic group with an emphasis on neurology, hence the minimalist-type brain logo. We want to convey that modern and technical aspect with professionalism and the elite nature of our practice environment.

```html
<!DOCTYPE html>
<html lang="en">
<head>
<meta charset="utf-8">
<title>Vantage Chiropractic – Business Card</title>
<link rel="stylesheet" href="https://fonts.googleapis.com/css2?family=Open+Sans:wght@300;400;700;800&family=Roboto:wght@300;400;700;900&display=swap">
<style>
  :root {
    --brand-blue: #4a80c2;
    --ink: #1d1d1d;
    --ink-soft: #6f6f6f;
    --paper: #ffffff;
    --backdrop: #e4e4e4;
    --rule-light: rgba(255,255,255,0.75);
  }
  * { margin: 0; padding: 0; box-sizing: border-box; }
  html, body {
    width: 902px; height: 1200px; overflow: hidden;
    background: var(--backdrop);
  }
  .canvas { position: relative; width: 902px; height: 1200px; }

  .card {
    position: absolute; left: 71px; width: 760px; height: 434px;
    box-shadow: 0 3px 10px rgba(0,0,0,0.18);
  }
  .card--front { top: 130px; background: var(--paper); font-family: "Roboto", sans-serif; color: var(--ink); }
  .card--back  { top: 636px; background: var(--brand-blue); font-family: "Open Sans", sans-serif; color: var(--paper); }

  /* Front */
  .front__accent { position: absolute; left: 742px; top: 75px; width: 18px; height: 140px; background: var(--brand-blue); }
  .brand--stacked { position: absolute; left: 40px; top: 190px; width: 255px; text-align: center; }
  .brand__dot { display: block; width: 110px; height: 110px; border-radius: 50%; background: var(--brand-blue); margin: 0 auto 22px; }
  .brand__name { font-family: "Roboto", sans-serif; font-weight: 400; font-size: 27px; line-height: 30px; letter-spacing: 1px; color: #333333; }

  .person { position: absolute; left: 333px; top: 62px; }
  .person__name { font-size: 35px; line-height: 40px; font-weight: 300; letter-spacing: 0.5px; }
  .person__name strong { font-weight: 900; }
  .person__creds { font-size: 21px; font-weight: 300; color: var(--ink-soft); margin-top: 2px; }

  .contact { position: absolute; left: 333px; top: 148px; list-style: none; font-size: 23px; font-weight: 300; }
  .contact li { display: flex; align-items: center; height: 30px; }
  .contact svg { width: 22px; margin-right: 10px; }

  .office { position: absolute; left: 333px; top: 306px; }
  .office__title { font-size: 20px; font-weight: 700; letter-spacing: 0.3px; }
  .office__line { font-size: 22px; font-weight: 300; line-height: 30px; }
  .office__title + .office__line { margin-top: 8px; }

  /* Back */
  .brand--inline { position: absolute; left: 145px; top: 62px; display: flex; align-items: center; }
  .brand--inline .brand__dot { width: 110px; height: 110px; margin: 0 22px 0 0; background: var(--paper); }
  .brand--inline .brand__name { font-family: "Open Sans", sans-serif; color: var(--paper); font-size: 38px; line-height: 44px; font-weight: 400; letter-spacing: 1px; }

  .cta { position: absolute; left: 47px; top: 250px; }
  .cta__ask { font-size: 29px; font-weight: 300; line-height: 36px; }
  .cta__action { font-size: 28px; font-weight: 800; line-height: 34px; letter-spacing: 0.5px; }
  .cta__web { position: absolute; left: 47px; top: 364px; font-size: 26px; font-weight: 300; white-space: nowrap; }
  .cta__web strong { font-weight: 700; }

  .locations { position: absolute; left: 360px; top: 248px; width: 355px; list-style: none; }
  .locations li { font-size: 22px; font-weight: 300; line-height: 38px; border-bottom: 1px solid var(--rule-light); white-space: nowrap; }
  .locations li:last-child { border-bottom: none; }
  .locations strong { font-weight: 700; }
</style>
</head>
<body>
<main class="canvas">

  <section class="card card--front" aria-label="Business card front">
    <div class="front__accent"></div>

    <div class="brand brand--stacked">
      <span class="brand__dot"></span>
      <p class="brand__name">VANTAGE<br>CHIROPRACTIC</p>
    </div>

    <header class="person">
      <h1 class="person__name">DR. <strong>JORDAN ELLERY</strong></h1>
      <p class="person__creds">DC, DACNB</p>
    </header>

    <ul class="contact">
      <li>
        <svg viewBox="0 0 22 28" aria-hidden="true"><rect x="4" y="2" width="14" height="24" rx="2" fill="none" stroke="#4a80c2" stroke-width="1.6"/><line x1="9" y1="22" x2="13" y2="22" stroke="#4a80c2" stroke-width="1.6"/></svg>
        (000) 000-0000
      </li>
      <li>
        <svg viewBox="0 0 22 16" aria-hidden="true"><rect x="1" y="2" width="20" height="13" fill="none" stroke="#4a80c2" stroke-width="1.6"/><polyline points="1,2 11,10 21,2" fill="none" stroke="#4a80c2" stroke-width="1.6"/></svg>
        jordan@vantagechiro.com
      </li>
    </ul>

    <address class="office" style="font-style:normal">
      <p class="office__title">FAIRBROOK OFFICE</p>
      <p class="office__line">218 Maple Ridge Rd.</p>
      <p class="office__line">Fairbrook, OH 43000</p>
    </address>
  </section>

  <section class="card card--back" aria-label="Business card back">
    <div class="brand brand--inline">
      <span class="brand__dot"></span>
      <p class="brand__name">VANTAGE<br>CHIROPRACTIC</p>
    </div>

    <div class="cta">
      <p class="cta__ask">QUESTIONS?</p>
      <p class="cta__action">CONTACT US</p>
    </div>
    <p class="cta__web">www.<strong>vantagechiro</strong>.com</p>

    <ul class="locations">
      <li>NORTHFIELD <strong>(555) 210-4400</strong></li>
      <li>OAK HOLLOW <strong>(555) 318-4400</strong></li>
      <li>FAIRBROOK <strong>(555) 426-WELL</strong></li>
      <li>STONEBRIDGE <strong>(555) 475-4400</strong></li>
    </ul>
  </section>

</main>
</body>
</html>
```